依頼詳細
屋外にタペストリーで掲げている店案内ですが、ショッピングセンター内にあるため屋外からエステだと一目でわかるものにしたいと考えております。そのためのデザインをお願いいたします。
記載項目
記載項目
特にエステティックであることをはっきりと掲載したいため「ロゴマーク」「エステティックサロン」「美顔」「痩身」「脱毛」というワードを大きく
続いて「電話番号」「営業時間」
また「店名」も掲載しますが目立たなくとも良いです。
ロゴマークは添付のものをご利用ください。
色ならびにロゴマーク中のグラデーションの変更はしないようにお願いいたします。
参考として旧タペストリーと他店の駐車場看板を添付します。
旧タペストリーのデザインとは全くかけ離れて構いません。
駐車場看板は見せ方の参考として添付します。店名よりもエステティックを強調しているという事の参考になればと思います。

店名 ルフィナ桜川店
電話番号 0296-41-6093
営業時間 9:30~20:30
サイズ:縦2400mm×横3200mm
希望イメージ
シンプル 複雑
単色 カラフル
暗い 明るい
日常 高級
遊び心 厳粛
未来的 伝統的
女性的 男性的
希望する色
設定なし
納品ファイル
• イラストレーター形式 (.ai)
• フォトショップ形式 (.psd)
補足説明
写真利用の場合は、納品の際は埋め込みではなくリンクでお願いします。
表記につきまして若干変更をさせていただきます、

「エステティックサロン」は英字よりカナ表記が目立つようにお願いいたします。
「美顔」→「フェイシャル」に変更(カナ表記)
「痩身」→「ボディ」に変更(カナ表記)
「脱毛」→変更なし

また女性の画像等はイメージやパーツとして使用いただいてもOKですが、スワンのマークをもう少し前面に出していただけたらと思います。
画像のイメージが前面にでるより、スワンのロゴが前面にでるようにできればと思います。イメージ画像等は全くないものでも可です。

添付でスワンのロゴのみのaiを追加いたします。

締め切りを変更させていただきます。

当方が伝えたいものが、しっかりと出ていて、色味も落ち着きがありながらロゴがはっきりと見えるデザインで好感が持てました。

本当にたくさんのデザインを頂きありがとうございます。

```html
<!DOCTYPE html>
<html lang="ja">
<head>
<meta charset="utf-8">
<title>エステティックサロン RUFINA タペストリー</title>
<link rel="stylesheet" href="https://fonts.googleapis.com/css2?family=Marcellus&family=Noto+Sans+JP:wght@500;700;900&display=swap">
<style>
  :root {
    --page-bg: #f4f4f4;
    --pink-light: #fbe6ee;
    --pink-mid: #f4c3d4;
    --pink-soft: #f8d6e2;
    --rose-accent: #e4566f;
    --title-glow: #e8508c;
    --grey-text: #5e5e5e;
    --dark-text: #444;
    --white: #ffffff;
  }
  * { margin: 0; padding: 0; box-sizing: border-box; }
  html, body {
    width: 1200px; height: 918px; overflow: hidden;
    background: var(--page-bg);
  }
  .tapestry {
    position: absolute; left: 34px; top: 34px;
    width: 1140px; height: 852px; overflow: hidden;
    box-shadow: 0 2px 8px rgba(0,0,0,0.25);
  }
  .rose-backdrop {
    position: absolute; inset: 0;
    background:
      radial-gradient(circle at 24% 58%, var(--pink-mid) 0, transparent 22%),
      radial-gradient(circle at 60% 75%, var(--pink-mid) 0, transparent 20%),
      radial-gradient(circle at 92% 86%, #f7d3cf 0, transparent 18%),
      radial-gradient(circle at 88% 40%, var(--pink-soft) 0, transparent 20%),
      linear-gradient(160deg, var(--pink-light) 0%, var(--pink-soft) 50%, var(--pink-light) 100%);
  }
  .headline {
    position: absolute; left: 0; right: 0; top: 60px;
    text-align: center;
    font-family: "Noto Sans JP", sans-serif; font-weight: 900;
    font-size: 96px; letter-spacing: 0; line-height: 1;
    color: var(--white);
    text-shadow: 0 0 6px var(--title-glow), 0 0 14px var(--title-glow), 0 0 24px rgba(232,80,140,0.6);
  }
  .services {
    position: absolute; left: 520px; top: 196px;
    font-family: "Noto Sans JP", sans-serif; font-weight: 900;
    font-size: 42px; line-height: 1;
    color: var(--grey-text);
    transform: skewX(-12deg);
    text-shadow: 0 0 6px var(--white), 0 0 10px var(--white);
  }
  .brand-dot {
    position: absolute; left: 96px; top: 290px;
    width: 330px; height: 330px; border-radius: 50%;
    background: rgba(228,86,111,0.18);
  }
  .brand-sub, .brand-name {
    position: absolute; left: 480px;
    font-family: "Marcellus", serif; font-weight: 400;
    color: var(--rose-accent); line-height: 1;
  }
  .brand-sub { top: 318px; font-size: 46px; }
  .brand-name { top: 388px; font-size: 134px; letter-spacing: 4px; }
  .shop-name {
    position: absolute; right: 76px; top: 522px;
    font-family: "Noto Sans JP", sans-serif; font-weight: 500;
    font-size: 16px; color: var(--dark-text);
  }
  .contact {
    position: absolute; left: 268px; top: 780px;
    display: flex; align-items: center; gap: 14px;
    font-family: "Noto Sans JP", sans-serif; font-weight: 700;
    color: var(--grey-text); line-height: 1;
  }
  .contact .phone { display: flex; align-items: center; gap: 4px; font-size: 26px; font-weight: 900; }
  .contact .hours { font-size: 24px; font-weight: 700; }
  .phone-icon { width: 26px; height: 26px; }
</style>
</head>
<body>
  <main class="tapestry">
    <div class="rose-backdrop" role="img" aria-label="淡いピンクのバラの花が一面に広がる背景写真"></div>

    <h1 class="headline">エステティックサロン</h1>
    <p class="services">フェイシャル／ボディ／脱毛</p>

    <div class="brand-dot"></div>
    <p class="brand-sub">Esthetic salon</p>
    <p class="brand-name">RUFINA</p>
    <p class="shop-name">ルフィナ桜川店</p>

    <div class="contact">
      <span class="phone">
        <svg class="phone-icon" viewBox="0 0 24 24" aria-hidden="true">
          <path d="M6.6 10.8a15.1 15.1 0 0 0 6.6 6.6l2.2-2.2c.3-.3.7-.4 1-.2 1.1.4 2.3.6 3.6.6.6 0 1 .4 1 1V20c0 .6-.4 1-1 1C10.6 21 3 13.4 3 4c0-.6.4-1 1-1h3.5c.6 0 1 .4 1 1 0 1.3.2 2.5.6 3.6.1.3 0 .7-.2 1z" fill="#5e5e5e"/>
        </svg>
        0296-41-6093
      </span>
      <span class="hours">営業時間 10:00-19:00</span>
    </div>
  </main>
</body>
</html>
```